Professionelles Webdesign für hochwertiges Coaching Business
Zielgruppe
Es geht um eine Coaching-Firma für Einzelcoaching, Team-Coaching in Firmen und Ausbildungen. Inhalt sind Kommunikation, Stressmanagement und Leistungssteigerung, Persönlichkeitsentwicklung bis hin zum Marketing für Coaches.
Aufgabenstellung
- siehe Briefing im Dateiupload
- Umsetzung via Baukastensystem. Wichtig ist, dass die Features mit dem Baukastensystem umsetzbar sind.
- Es dürfen bitte diese 4 Seiten gestaltet werden:
Startseite
Coaching
Training
Ausbildung
- Obgleich ich Kundenfokus auf der Website bevorzuge, darf sie mich auch etwas widerspiegeln. Für einen Eindruck über mich sind zwei Bilder dem Anhang beigefügt. Diese Bilder sollen NICHT in die Website eingebunden werden.

```html
<!DOCTYPE html>
<html lang="de">
<head>
<meta charset="utf-8">
<title>Hallberg – Training &amp; Coaching</title>
<link href="https://fonts.googleapis.com/css2?family=Abel&family=Source+Code+Pro:wght@400;600&display=swap" rel="stylesheet">
<style>
  :root {
    --ink: #1c1c1c;
    --white: #ffffff;
    --band: #629bba;
    --hero-dark: #6a5f58;
    --hero-mid: #8a7f77;
    --hero-light: #a39d97;
    --help: #0d0d0d;
  }
  * { box-sizing: border-box; margin: 0; padding: 0; }
  html, body { width: 1131px; height: 1200px; overflow: hidden; background: var(--white); }
  body { position: relative; font-family: "Abel", sans-serif; color: var(--ink); }

  .site-header { position: absolute; left: 0; top: 0; width: 1131px; height: 126px; border-top: 1px solid #e6e6e6; }
  .brand { position: absolute; left: 55px; top: 46px; display: flex; align-items: center; gap: 12px; }
  .brand-dot { width: 34px; height: 34px; border-radius: 50%; background: #9b2a2f; }
  .brand-name { font-family: "Source Code Pro", monospace; font-weight: 600; font-size: 24px; letter-spacing: 2px; color: #2a2a2a; }

  .main-nav { position: absolute; top: 56px; left: 453px; display: flex; align-items: center; gap: 20px;
    font-family: "Source Code Pro", monospace; font-size: 17px; letter-spacing: 0.5px; }
  .main-nav a { color: var(--ink); text-decoration: none; }
  .nav-network { font-weight: 600; font-size: 13px; margin-left: 4px; }
  .nav-mail { margin-left: 4px; display: block; }

  .hero { position: absolute; left: 2px; top: 126px; width: 1129px; height: 656px; overflow: hidden; }
  .hero-photo { position: absolute; inset: 0;
    background: linear-gradient(90deg, var(--hero-light) 0%, var(--hero-mid) 35%, var(--hero-dark) 60%, var(--hero-mid) 85%, var(--hero-light) 100%); }
  .hero-links { position: absolute; left: 177px; top: 118px; list-style: none; }
  .hero-links li { height: 104px; }
  .hero-links a { color: var(--white); text-decoration: none; font-size: 62px; line-height: 68px;
    display: inline-block; border-bottom: 1.5px solid var(--white); }

  .intro-band { position: absolute; left: 2px; top: 782px; width: 1129px; height: 360px; background: var(--band);
    color: var(--white); text-align: center; }
  .intro-text { position: absolute; left: 0; right: 0; top: 80px; font-size: 33px; line-height: 44px; }
  .intro-lead { position: absolute; left: 0; right: 0; top: 200px; font-size: 33px; line-height: 44px; }
  .cta { position: absolute; left: 394px; top: 271px; width: 342px; height: 65px; border: 2px solid var(--white);
    color: var(--white); text-decoration: none; font-family: "Source Code Pro", monospace; font-weight: 600;
    font-size: 17px; letter-spacing: 1.5px; display: flex; align-items: center; justify-content: center; }

  .help-button { position: absolute; left: 1038px; top: 1095px; width: 58px; height: 58px; border-radius: 50%;
    background: var(--help); color: var(--white); font-family: "Source Code Pro", monospace; font-size: 24px;
    display: flex; align-items: center; justify-content: center; box-shadow: 0 2px 6px rgba(0,0,0,.3); }
</style>
</head>
<body>
  <header class="site-header">
    <div class="brand">
      <span class="brand-dot"></span>
      <span class="brand-name">HALLBERG</span>
    </div>
    <nav class="main-nav">
      <a href="#">Coaching</a>
      <a href="#">Training</a>
      <a href="#">Ausbildungen</a>
      <a href="#">Unternehmen</a>
      <a href="#">Methoden</a>
      <a href="#" class="nav-network">Netzwerk</a>
      <a href="#" class="nav-mail" aria-label="E-Mail">
        <svg width="18" height="13" viewBox="0 0 18 13"><rect x="1" y="1" width="16" height="11" fill="none" stroke="#1c1c1c" stroke-width="2"/><path d="M1 1 L9 7 L17 1" fill="none" stroke="#1c1c1c" stroke-width="2"/></svg>
      </a>
    </nav>
  </header>

  <section class="hero">
    <div class="hero-photo" role="img" aria-label="Foto: Coachin mit Umhängeband spricht lächelnd vor einer Wand mit Urkunden"></div>
    <ul class="hero-links">
      <li><a href="#">Coaching</a></li>
      <li><a href="#">Training</a></li>
      <li><a href="#">Blog</a></li>
      <li><a href="#">Methoden</a></li>
    </ul>
  </section>

  <section class="intro-band">
    <p class="intro-text">Das ist in ein Blindtext. Hier erhalten Sie einen Überblick zu<br>meinen Dienstleistungen.</p>
    <p class="intro-lead">Bei mir finden Sie diese Dienstleistungen.</p>
    <a href="#" class="cta">Dienstleistungen entdecken</a>
  </section>

  <div class="help-button">?</div>
</body>
</html>
```